The Cedarline Outreach
United in service through passion for Christ
I need double sided standard sized Business Card [3.5" x 2"]
I would stay away from cursive, but don't have any certain requests as to what font is used.
Simple
Daniel Whitacre
Director
4830 Birchmont Lane
Greensboro, NC 27408
daniel@cedarlineoutreach.com
cedarlineoutreach.com
The LORD will guide you always; He will satisfy your needs in a sun-scorched land
and will strengthen your frame. You will be like a well-watered garden, like a spring whose waters never fail. Isaiah 58:11

```html
<!DOCTYPE html>
<html lang="en">
<head>
<meta charset="utf-8">
<title>The Cedarline Outreach — Stationery</title>
<link href="https://fonts.googleapis.com/css2?family=Open+Sans:wght@400;600;700&display=swap" rel="stylesheet">
<style>
:root{
  --bg:#e9eaec;
  --dark:#1b1e22;
  --dark-2:#2a2e33;
  --paper:#ffffff;
  --blue:#1c5fae;
  --blue-deep:#0f3f82;
  --green:#5cb531;
  --green-light:#8ccf4a;
  --ink:#3a3f45;
  --muted:#8b9096;
  --faint:#eef0f2;
}
*{box-sizing:border-box;margin:0;padding:0}
html,body{width:1200px;height:313px;overflow:hidden}
body{background:var(--bg);font-family:"Open Sans",Arial,sans-serif;position:relative;color:var(--ink)}
.piece{position:absolute;box-shadow:0 1px 4px rgba(0,0,0,.25);overflow:hidden}
.brand{display:flex;align-items:center;gap:4px;font-weight:700;color:var(--blue);white-space:nowrap}
.brand-dot{border-radius:50%;background:var(--green);flex:none}

/* presentation panel */
.panel{position:absolute;left:0;top:0;width:300px;height:313px;background:linear-gradient(90deg,var(--dark),var(--dark-2) 50%,var(--dark));}
.panel .brand{position:absolute;left:16px;top:64px;font-size:15px;color:#fff}
.panel .brand-dot{width:16px;height:16px}
.panel-caption{position:absolute;left:38px;top:86px;font-size:6px;color:var(--muted);letter-spacing:.5px}

/* business cards */
.card{top:205px;width:122px;height:70px;background:var(--paper)}
.card-front{left:12px}
.card-back{left:140px;background:linear-gradient(160deg,var(--blue),var(--blue-deep))}
.card-front .brand{position:absolute;left:6px;top:8px;font-size:6.5px}
.card-front .brand-dot{width:8px;height:8px}
.card-front .details{position:absolute;left:8px;top:30px;font-size:3.6px;line-height:5px;color:var(--ink)}
.card-front .details strong{font-size:4.4px;color:var(--blue)}
.card-back .brand{position:absolute;left:24px;top:28px;font-size:7px;color:#fff}
.card-back .brand-dot{width:9px;height:9px}
.card .wave{position:absolute;left:0;bottom:0;width:100%;height:18px}

/* letterheads */
.letterhead{top:19px;width:156px;height:269px;background:var(--paper)}
.letterhead-1{left:307px}
.letterhead-2{left:480px}
.letterhead .brand{position:absolute;left:12px;top:12px;font-size:6px}
.letterhead .brand-dot{width:8px;height:8px}
.letterhead .contact{position:absolute;right:14px;top:12px;font-size:3px;line-height:4px;color:var(--muted);text-align:left}
.letterhead .mark{position:absolute;left:53px;top:110px;width:50px;height:50px;border-radius:50%;background:var(--faint)}
.letterhead .wave{position:absolute;left:0;bottom:0;width:100%;height:30px}

/* envelopes */
.envelope{left:696px;width:180px;height:82px;background:var(--paper)}
.envelope-1{top:96px}
.envelope-2{top:188px}
.envelope .brand{position:absolute;left:8px;top:8px;font-size:6px}
.envelope .brand-dot{width:7px;height:7px}
.envelope .return{position:absolute;left:8px;top:19px;font-size:3px;line-height:4px;color:var(--muted)}
.envelope .wave{position:absolute;left:0;bottom:0;width:100%;height:20px}

/* envelope backs */
.env-back{left:900px;width:240px;height:80px;background:var(--paper)}
.env-back-1{top:22px;background:linear-gradient(180deg,var(--green-light),var(--green) 40%,var(--blue) 100%)}
.env-back-2{top:108px}
.env-back-3{top:196px}
.env-back svg{position:absolute;inset:0;width:100%;height:100%}
.env-back .seal{position:absolute;left:112px;top:22px;width:16px;height:16px;border-radius:50%;background:var(--paper)}
.env-back-2 .seal{background:var(--green)}
</style>
</head>
<body>

<section class="panel">
  <div class="brand"><span class="brand-dot"></span>The Cedarline Outreach</div>
  <p class="panel-caption">Stationery Design</p>
</section>

<article class="piece card card-front">
  <div class="brand"><span class="brand-dot"></span>The Cedarline Outreach</div>
  <div class="details">
    <strong>Daniel Whitacre</strong><br>Director<br>4830 Birchmont Lane<br>Greensboro, NC 27408<br>daniel@cedarlineoutreach.com<br>cedarlineoutreach.com
  </div>
  <svg class="wave" viewBox="0 0 122 18" preserveAspectRatio="none"><path d="M0 12 Q60 2 122 8 V18 H0Z" fill="var(--green)"/><path d="M0 15 Q60 6 122 12 V18 H0Z" fill="var(--blue)"/></svg>
</article>

<article class="piece card card-back">
  <div class="brand"><span class="brand-dot"></span>The Cedarline Outreach</div>
</article>

<article class="piece letterhead letterhead-1">
  <div class="brand"><span class="brand-dot"></span>The Cedarline Outreach</div>
  <div class="contact">4830 Birchmont Lane<br>Greensboro, NC 27408<br>cedarlineoutreach.com</div>
  <div class="mark"></div>
  <svg class="wave" viewBox="0 0 156 30" preserveAspectRatio="none"><path d="M0 20 Q80 8 156 16 V30 H0Z" fill="var(--green)"/><path d="M0 25 Q80 12 156 22 V30 H0Z" fill="var(--blue)"/></svg>
</article>

<article class="piece letterhead letterhead-2">
  <div class="brand"><span class="brand-dot"></span>The Cedarline Outreach</div>
  <div class="mark"></div>
  <svg class="wave" viewBox="0 0 156 30" preserveAspectRatio="none"><path d="M0 20 Q80 8 156 16 V30 H0Z" fill="var(--green)"/><path d="M0 25 Q80 12 156 22 V30 H0Z" fill="var(--blue)"/></svg>
</article>

<article class="piece envelope envelope-1">
  <div class="brand"><span class="brand-dot"></span>The Cedarline Outreach</div>
  <div class="return">4830 Birchmont Lane<br>Greensboro, NC 27408</div>
  <svg class="wave" viewBox="0 0 180 20" preserveAspectRatio="none"><path d="M0 12 Q90 2 180 9 V20 H0Z" fill="var(--green)"/><path d="M0 16 Q90 6 180 13 V20 H0Z" fill="var(--blue)"/></svg>
</article>

<article class="piece envelope envelope-2">
  <div class="brand"><span class="brand-dot"></span>The Cedarline Outreach</div>
  <div class="return">4830 Birchmont Lane<br>Greensboro, NC 27408</div>
  <svg class="wave" viewBox="0 0 180 20" preserveAspectRatio="none"><path d="M0 12 Q90 2 180 9 V20 H0Z" fill="var(--green)"/><path d="M0 16 Q90 6 180 13 V20 H0Z" fill="var(--blue)"/></svg>
</article>

<article class="piece env-back env-back-1">
  <svg viewBox="0 0 240 80" preserveAspectRatio="none"><path d="M0 0 L120 48 L240 0" fill="none" stroke="rgba(255,255,255,.35)" stroke-width="1"/></svg>
  <div class="seal"></div>
</article>

<article class="piece env-back env-back-2">
  <svg viewBox="0 0 240 80" preserveAspectRatio="none"><path d="M0 0 H240 L120 50Z" fill="var(--blue)"/><path d="M0 80 L120 40 L240 80" fill="none" stroke="#d6d9dc" stroke-width="1"/></svg>
  <div class="seal"></div>
</article>

<article class="piece env-back env-back-3">
  <svg viewBox="0 0 240 80" preserveAspectRatio="none"><path d="M0 0 L120 48 L240 0" fill="none" stroke="#d6d9dc" stroke-width="1"/><path d="M0 80 L120 40 L240 80" fill="none" stroke="#d6d9dc" stroke-width="1"/></svg>
</article>

</body>
</html>
```